Luxury Photoalbum manufacturer needs banner design 8'x8'

We need a banner design for trade show purposes. We supply luxury one-of-a-kind photo albums to boudoir photographers. Our customers are female professional photographers - mostly in the age range of 26 - 40.Design needs to appeal to business women in this age range who see their business help empower women.Follow our website for our current look and feel. www.velvetkeepsake.com
It needs to be 8'x8'

Target Market(s)

Women professional boudoir photographers

Industry/Entity Type

Professional Photography

Font styles to use
Serif

Requirements
Must have
• Feminine but professional look and feel
• Need the LOGO to be very dominant
• Needs to be reasonably consistent with our website - www.velvetkeepsake.com
Nice to have
• Not necessary to use all the images - can use as few or many as makes sense.

```html
<!DOCTYPE html>
<html lang="en">
<head>
<meta charset="utf-8">
<title>Velvet Keepsake – Albums that fit your Brand</title>
<link rel="stylesheet" href="https://fonts.googleapis.com/css2?family=Playfair+Display:wght@400&display=swap">
<style>
  :root {
    --brand-red: #ec1f27;
    --night: #0b0809;
    --wine: #3a0d16;
    --umber: #2a2220;
    --sand: #b4977c;
    --ivory: #ffffff;
    --rose-foil: #c9a7a4;
  }
  html, body {
    margin: 0;
    padding: 0;
    width: 1200px;
    height: 1200px;
    overflow: hidden;
    background: var(--sand);
  }
  .banner {
    position: relative;
    width: 1200px;
    height: 1200px;
    overflow: hidden;
    font-family: "Playfair Display", Georgia, serif;
  }
  .banner__shapes {
    position: absolute;
    inset: 0;
    width: 1200px;
    height: 1200px;
  }
  .banner__headline {
    position: absolute;
    top: 62px;
    left: 0;
    width: 1200px;
    margin: 0;
    text-align: center;
    color: var(--ivory);
    font-weight: 400;
    font-size: 73px;
    line-height: 1.2;
    letter-spacing: 0.5px;
  }
  .banner__brand {
    position: absolute;
    top: 480px;
    left: 0;
    width: 1200px;
    margin: 0;
    text-align: center;
    color: var(--rose-foil);
    font-weight: 400;
    font-size: 112px;
    line-height: 1.1;
  }
  .banner__url {
    position: absolute;
    top: 1066px;
    left: 0;
    width: 1200px;
    margin: 0;
    text-align: center;
    color: var(--ivory);
    font-size: 33px;
    letter-spacing: 6px;
  }
</style>
</head>
<body>
  <main class="banner">
    <svg class="banner__shapes" viewBox="0 0 1200 1200" xmlns="http://www.w3.org/2000/svg">
      <defs>
        <linearGradient id="album-stack-tones" x1="0" y1="0" x2="1" y2="1">
          <stop offset="0" stop-color="var(--wine)"/>
          <stop offset="0.45" stop-color="var(--night)"/>
          <stop offset="0.75" stop-color="var(--umber)"/>
          <stop offset="1" stop-color="var(--night)"/>
        </linearGradient>
      </defs>
      <rect class="band band--sand" x="0" y="0" width="1200" height="1200" fill="var(--sand)"/>
      <polygon class="band band--red" points="0,0 1200,0 1200,207 0,298" fill="var(--brand-red)"/>
      <polygon class="band band--photo" role="img"
        aria-label="Photograph of stacked textured leather albums in wine and black with strands of pearls, dimly lit"
        points="0,298 1200,207 1200,915 0,1005" fill="url(#album-stack-tones)"/>
    </svg>

    <h1 class="banner__headline">Albums that fit your Brand</h1>
    <p class="banner__brand">Velvet Keepsake</p>
    <p class="banner__url">www.velvetkeepsake.com</p>
  </main>
</body>
</html>
```